Design Rum Bottle Label

I want a design for a Rum bottle i want to release.
For now it is planned to call the Rum Kelvoort Dark SpicedRum, like the name of my liqoir store but that is open for change if there is a better proposal.
The design is free, but it should certainly be stylish and radiate that this is a very high-quality product. I attach my logo but it is not a must to process this in the design.

There should be 2 labels, one for the front and one for the back.
what should be included in the front logo:
- Limited edition
- bottle ... / 500 (the bottle number is filled in by hand)
- 38% Vol.
- ℮ 70cl

What should be included on the back logo:
- small symbol recyclable
- small symbol forbidden for pregnant woman
- kelvoort logo (is in attachement)
- in small: produced by 7315 Velvet Lodge

I am adding a photo with the shape of the bottle so that you can take this into account.
The size of the ticket is provided at 9.5cm x 9.5cm.

By entering this competition you agree, if you win, that any minor changes to the design can still be made. If you win, you will receive the agreed amount and in return the design will be delivered in a usable file format in good quality.
By receiving the sum you agree that all rights to this design become the property of ww.kelvoort-example.be and that you may no longer use this design for any other purpose.

```html
<!DOCTYPE html>
<html lang="en">
<head>
<meta charset="utf-8">
<title>Kelvoort Dark Rum – Front Label</title>
<link rel="stylesheet" href="https://fonts.googleapis.com/css2?family=Rye&family=Graduate&family=Roboto:wght@400&family=Roboto+Slab:wght@400&display=swap">
<style>
  :root {
    --stage: #ececec;
    --label-black: #0b0b0b;
    --gold: #c9974f;
    --gold-light: #e6c48a;
    --gold-dark: #8a5f2a;
    --white: #ffffff;
    --ink: #1a1a1a;
  }
  html, body {
    margin: 0;
    padding: 0;
    width: 746px;
    height: 1200px;
    overflow: hidden;
    background: var(--stage);
  }
  .canvas {
    position: relative;
    width: 746px;
    height: 1200px;
  }
  .front-label {
    position: absolute;
    left: 43px;
    top: 270px;
    width: 660px;
    height: 660px;
    display: block;
  }
  .brand-name {
    font-family: "Rye", serif;
    font-size: 88px;
    fill: var(--gold);
    letter-spacing: 1px;
  }
  .product-type {
    font-family: "Graduate", serif;
    font-size: 40px;
    fill: var(--white);
    letter-spacing: 4px;
  }
  .edition {
    font-family: "Roboto Slab", serif;
    font-size: 27px;
    font-weight: 400;
    fill: var(--white);
    letter-spacing: 2px;
  }
  .volume {
    font-family: "Roboto", sans-serif;
    font-size: 19px;
    fill: var(--white);
  }
  .bottle-number {
    font-family: "Roboto", sans-serif;
    font-size: 17px;
    fill: var(--ink);
  }
  .star { fill: var(--gold); }
  .rule { stroke: var(--gold); fill: none; }
  .ornament { fill: var(--gold-dark); opacity: 0.55; }
</style>
</head>
<body>
<main class="canvas">
  <svg class="front-label" viewBox="0 0 660 660" xmlns="http://www.w3.org/2000/svg" role="group" aria-label="Kelvoort Dark Rum front label">
    <defs>
      <linearGradient id="gold-sheen" x1="0" x2="1" y1="0" y2="0">
        <stop offset="0" stop-color="#b47d3c"/>
        <stop offset="0.5" stop-color="#e0b877"/>
        <stop offset="1" stop-color="#a8702f"/>
      </linearGradient>
      <path id="edition-arc" d="M150,392 Q330,500 510,392"/>
    </defs>

    <!-- label ground and frame -->
    <rect class="label-ground" width="660" height="660" fill="var(--label-black)"/>
    <rect class="rule frame-outer" x="14" y="14" width="632" height="632" stroke-width="1.5"/>

    <!-- corner ornaments -->
    <rect class="ornament" x="22" y="22" width="100" height="100" rx="10" role="img" aria-label="Gold scroll ornament, top left corner"/>
    <rect class="ornament" x="538" y="22" width="100" height="100" rx="10" role="img" aria-label="Gold scroll ornament, top right corner"/>
    <rect class="ornament" x="22" y="538" width="100" height="100" rx="10" role="img" aria-label="Gold scroll ornament, bottom left corner"/>
    <rect class="ornament" x="538" y="538" width="100" height="100" rx="10" role="img" aria-label="Gold scroll ornament, bottom right corner"/>

    <!-- top flourish -->
    <rect class="ornament" x="200" y="40" width="260" height="115" rx="14" role="img" aria-label="Gold flourish crest with a small star above the name"/>

    <!-- upper rule -->
    <line class="rule" x1="40" y1="170" x2="620" y2="170" stroke-width="2"/>

    <!-- brand -->
    <text class="brand-name" x="330" y="268" text-anchor="middle" textLength="560" lengthAdjust="spacingAndGlyphs">KELVOORT</text>

    <!-- product line with stars -->
    <line class="rule" x1="40" y1="298" x2="620" y2="298" stroke-width="1.5"/>
    <g class="stars-left">
      <polygon class="star" points="100,345 104,355 115,355 106,361 110,372 100,365 90,372 94,361 85,355 96,355"/>
      <polygon class="star" points="135,345 139,355 150,355 141,361 145,372 135,365 125,372 129,361 120,355 131,355"/>
      <polygon class="star" points="170,345 174,355 185,355 176,361 180,372 170,365 160,372 164,361 155,355 166,355"/>
    </g>
    <text class="product-type" x="330" y="372" text-anchor="middle">DARK RUM</text>
    <g class="stars-right">
      <polygon class="star" points="490,345 494,355 505,355 496,361 500,372 490,365 480,372 484,361 475,355 486,355"/>
      <polygon class="star" points="525,345 529,355 540,355 531,361 535,372 525,365 515,372 519,361 510,355 521,355"/>
      <polygon class="star" points="560,345 564,355 575,355 566,361 570,372 560,365 550,372 554,361 545,355 556,355"/>
    </g>

    <!-- engraved horizontal lines -->
    <g class="rule engraving" stroke-width="1" opacity="0.8">
      <line x1="40" y1="392" x2="620" y2="392"/>
      <line x1="40" y1="406" x2="620" y2="406"/>
      <line x1="40" y1="420" x2="620" y2="420"/>
      <line x1="40" y1="434" x2="620" y2="434"/>
      <line x1="40" y1="448" x2="620" y2="448"/>
      <line x1="40" y1="462" x2="620" y2="462"/>
      <line x1="40" y1="476" x2="620" y2="476"/>
      <line x1="40" y1="490" x2="620" y2="490"/>
      <line x1="40" y1="504" x2="620" y2="504"/>
      <line x1="40" y1="518" x2="620" y2="518"/>
      <line x1="40" y1="532" x2="620" y2="532"/>
      <line x1="40" y1="546" x2="620" y2="546"/>
      <line x1="40" y1="560" x2="620" y2="560"/>
      <line x1="40" y1="574" x2="620" y2="574"/>
      <line x1="40" y1="588" x2="620" y2="588"/>
      <line x1="40" y1="602" x2="620" y2="602"/>
      <line x1="40" y1="616" x2="620" y2="616"/>
    </g>

    <!-- black field inside the arc -->
    <path d="M120,384 L540,384 L540,400 Q330,530 120,400 Z" fill="var(--label-black)"/>

    <!-- sunburst rays -->
    <g class="rule rays" stroke-width="1.2">
      <line x1="330" y1="386" x2="330" y2="410"/>
      <line x1="300" y1="388" x2="306" y2="410"/>
      <line x1="360" y1="388" x2="354" y2="410"/>
      <line x1="272" y1="390" x2="284" y2="410"/>
      <line x1="388" y1="390" x2="376" y2="410"/>
      <line x1="246" y1="392" x2="262" y2="410"/>
      <line x1="414" y1="392" x2="398" y2="410"/>
    </g>

    <!-- arc and edition text -->
    <text class="edition"><textPath href="#edition-arc" startOffset="50%" text-anchor="middle">LIMITED EDITION</textPath></text>
    <path class="rule" d="M130,412 Q330,530 530,412" stroke="url(#gold-sheen)" stroke-width="2.5"/>

    <!-- small lower flourish -->
    <rect class="ornament" x="290" y="478" width="80" height="40" rx="8" role="img" aria-label="Small gold scroll below the arc"/>

    <!-- volume -->
    <rect x="205" y="525" width="100" height="28" fill="var(--label-black)"/>
    <rect x="368" y="522" width="96" height="32" fill="var(--label-black)"/>
    <text class="volume" x="255" y="546" text-anchor="middle">38% Vol.</text>
    <text class="volume" x="416" y="547" text-anchor="middle" font-size="22">℮ 70cl</text>

    <!-- bottle number box -->
    <rect x="247" y="612" width="166" height="30" fill="var(--white)"/>
    <text class="bottle-number" x="263" y="633">bottle</text>
    <text class="bottle-number" x="358" y="633">/ 500</text>
  </svg>
</main>
</body>
</html>
```